Professional Website Design to match new logo for Medical Legal Company

We have rebranded our company and We want a professional but also dynamic web site design for a group of esteemed doctors that provide expert evaluation of an injured worker in a Workers Compensation case.
​
1. Our target market is both the attorneys who select our doctors and any doctors who would wish to join our group.

2. Notes for the Landing Page:
- We prefer a simpler, sleeker more modern look for the landing page.
- We want a simplified landing page with one image, three buttons highlighted in Content document.
- We want the main image to be black and white but it can be splashed with color.
-We think the landing page might be enhanced by add a dark blue or black as a primary color. Of course please feel free to try any color combination you think might work.
- We want "The Meridale Circle" in large letters and "Stewards of a fair and prompt outcome" in small lettering. We don't want icons on the buttons.
- Do not want more than the one picture at top of landing page.
- We do not want any pictures that include faces. Please eliminate or replace. They will not be chosen.
- For the landing page, instead of a second set of photos please experiment with using medical symbols and legal symbols.
​
3. New Company Name: The Meridale Circle
New logo is uploaded bronze and grey/silver will be colors although we are still tweaking the colors for more metallic feel. Want simple not busy.

4. The overall Web page design needs to have some website design effect (e,g image rollover, scrolling effect, hover effect etc).

5. Please follow the attached word document file for the page content of the 4 web pages. Do not mix it up.

Previous company website: www.clinicjuristpanel.example (we wish to convert some of the content from this website to the new brand). Competitor website that we like: www.docboardly.example

Target Market(s)

Professional Elite. Attorneys and Doctors

Industry/Entity Type

Medical Legal

Coding

Coded - Design and coding required

Number of Pages Required

5+ page

Font styles to use
Other font styles liked:
• Helvetica or maybe font that matches logo. We are open

Colors

Designer to choose colors to be used in the design.

Requirements
Must have
• I can't locate on color scale but we want Bronze and Silver/Grey from logo. Additional colors can be added. Various shades of grey
Nice to have
• Black and white photos, simple elegant design
Should not have
• Images with faces of unknown people

```html
<!DOCTYPE html>
<html lang="en">
<head>
<meta charset="utf-8">
<title>The Meridale Circle — Medical-Legal Evaluations</title>
<link rel="stylesheet" href="https://fonts.googleapis.com/css2?family=Poppins:wght@400;500;600;700&display=swap">
<style>
:root{
  --bronze:#a3412a;
  --bronze-dark:#8a3520;
  --ink:#17171c;
  --night:#111116;
  --text:#333;
  --muted:#777;
  --light:#f2f2f2;
  --field:#eeeeee;
  --silver:#d9d9d9;
  --steel:#8e8e8e;
  --white:#fff;
}
*{box-sizing:border-box;margin:0;padding:0}
html,body{width:1200px;height:5071px;overflow:hidden}
body{position:relative;font-family:"Poppins",sans-serif;color:var(--text);background:var(--white)}
.abs{position:absolute}
.btn{position:absolute;display:flex;align-items:center;justify-content:center;color:var(--white);background:var(--bronze);font-weight:500;text-transform:uppercase;letter-spacing:.3px}
.h2{position:absolute;font-weight:700;color:var(--ink);text-transform:uppercase;letter-spacing:.3px}
.symbol{position:absolute;display:flex;align-items:center;justify-content:center}
.symbol.silver{background:linear-gradient(135deg,#ececec,#c9c9c9)}
.symbol.steel{background:linear-gradient(135deg,#5a5a5a,#9a9a9a)}
.symbol.bronze{background:linear-gradient(135deg,#b4533a,#8a3520)}

/* header */
.site-header{position:absolute;left:0;top:0;width:1200px;height:112px;background:var(--ink)}
.topbar{position:absolute;left:598px;top:0;width:602px;height:40px;background:var(--bronze);border-bottom-left-radius:26px;color:var(--white);font-weight:600;font-size:20px;display:flex;align-items:center}
.topbar .phone{position:absolute;left:30px;display:flex;align-items:center;gap:12px}
.topbar .join{position:absolute;right:42px;font-size:19px}
.brand{position:absolute;left:28px;top:14px;width:320px;height:90px;display:flex;align-items:center;gap:14px;color:#d6d6d6;font-size:30px;font-weight:600;letter-spacing:1px;line-height:1}
.brand .mark{width:34px;height:34px;background:var(--bronze)}
.brand small{display:block;font-size:16px;color:var(--bronze);letter-spacing:6px;margin-top:6px;text-align:center}
.nav{position:absolute;left:454px;top:70px;display:flex;gap:38px;font-size:15px;color:#cfcfcf}
.nav .active{text-decoration:underline;text-underline-offset:4px}
.login{position:absolute;left:1052px;top:70px;width:94px;height:24px;background:#9a9a9a;color:var(--white);font-size:13px;display:flex;align-items:center;justify-content:center}

/* hero */
.hero{position:absolute;left:0;top:112px;width:1200px;height:745px;background:linear-gradient(90deg,#f4f4f4 0%,#dcdcdc 35%,#9c9c9c 60%,#6e6e6e 80%,#b8b8b8 100%)}
.hero h1{position:absolute;left:36px;top:142px;width:520px;font-size:54px;line-height:63px;font-weight:700;color:var(--ink)}
.hero .slogan{position:absolute;left:36px;top:282px;width:520px;font-size:18px;line-height:24px;font-weight:600;color:var(--bronze);text-transform:uppercase;letter-spacing:.5px}
.hero p{position:absolute;left:36px;top:336px;width:520px;font-size:19px;line-height:24px;color:#222}
.hero .dot{position:absolute;top:657px;width:22px;height:22px;border-radius:50%;background:var(--ink)}

/* about */
.about-title{left:622px;top:994px;font-size:37px;line-height:46px}
.about-copy{position:absolute;left:622px;top:1098px;width:505px;font-size:13px;line-height:20.5px;color:#444}

/* features */
.features{position:absolute;left:62px;top:1408px;width:1062px;height:182px;background:var(--white);border-radius:12px;box-shadow:0 4px 24px rgba(0,0,0,.08)}
.feature{position:absolute;top:52px;display:flex;gap:16px}
.feature svg{flex:none}
.feature h3{font-size:14px;line-height:18px;font-weight:600;color:var(--ink);text-transform:uppercase}
.feature p{font-size:12px;line-height:15px;color:#555;margin-top:4px}

/* what we do */
.wwd{position:absolute;left:0;top:2110px;width:1200px;height:160px;background:var(--light)}
.section-sub{position:absolute;left:250px;width:700px;text-align:center;font-size:13px;line-height:19px;color:#666}
.card{position:absolute;width:260px;height:365px;background:var(--white);box-shadow:0 4px 20px rgba(0,0,0,.1)}
.card .symbol{left:-20px;top:0;width:255px;height:212px}
.card h3{position:absolute;left:14px;top:222px;width:220px;font-size:14px;line-height:17px;font-weight:600;color:var(--ink)}
.card p{position:absolute;left:14px;top:262px;width:220px;font-size:9.5px;line-height:13px;color:#777}
.card .btn{left:14px;top:326px;width:88px;height:24px;font-size:10px}
.arrow{position:absolute;top:1934px}

/* standard */
.std-title{left:100px;top:2340px;font-size:35px;line-height:45px}
.std-list{position:absolute;left:104px;top:2440px;width:520px;list-style:none}
.std-list li{position:relative;padding-left:28px;font-size:12.5px;line-height:18px;color:#444;margin-bottom:19px}
.std-list li svg{position:absolute;left:0;top:2px}

/* team */
.team{position:absolute;left:0;top:2800px;width:1200px;height:568px;background:var(--light)}
.member{position:absolute;top:188px;width:236px;height:230px;background:var(--white);text-align:center}
.member .initials{position:absolute;left:62px;top:24px;width:112px;height:112px;border-radius:50%;background:linear-gradient(135deg,#e2e2e2,#a9a9a9);display:flex;align-items:center;justify-content:center;font-size:30px;font-weight:600;color:var(--white)}
.member h4{position:absolute;left:0;right:0;top:164px;font-size:14px;font-weight:600;color:var(--ink)}
.member span{position:absolute;left:0;right:0;top:188px;font-size:12px;color:var(--bronze)}
.tdot{position:absolute;top:3294px;width:22px;height:22px;border-radius:50%;background:var(--ink)}

/* contact */
.contact{position:absolute;left:0;top:3368px;width:1200px;height:642px;background:linear-gradient(90deg,#2c3136,#4c5257 55%,#585858)}
.region{position:absolute;color:var(--white);font-weight:600;font-size:25px;line-height:28px;text-align:center}
.region small{display:block;font-size:9px;font-weight:400;color:#ddd;margin-top:6px}
.form-card{position:absolute;left:598px;top:3485px;width:537px;height:505px;background:var(--white);border-radius:14px}
.form-card h2{position:absolute;left:0;right:0;top:46px;text-align:center;font-size:34px;font-weight:700;color:var(--ink)}
.field{position:absolute;left:34px;width:463px;background:var(--field);font-size:13px;font-weight:500;color:#333;padding:22px 0 0 32px}
.submit{left:34px;top:425px;width:463px;height:60px;border-radius:14px;font-size:21px;font-weight:700}

/* blog */
.post{position:absolute;top:4225px;width:275px;height:388px;border:1px solid #ddd;background:var(--white);text-align:center}
.post .symbol{left:0;top:0;width:273px;height:195px}
.post h3{position:absolute;left:0;right:0;top:224px;font-size:18px;font-weight:700;color:var(--ink)}
.post p{position:absolute;left:22px;right:22px;top:264px;font-size:9px;line-height:16px;color:#777;text-transform:uppercase}
.post a{position:absolute;left:0;right:0;top:346px;font-size:13px;font-weight:600;color:var(--bronze);text-decoration:none}

/* footer */
.footer{position:absolute;left:0;top:4690px;width:1200px;height:381px;background:var(--night);color:#bbb}
.footer h5{position:absolute;top:102px;font-size:19px;font-weight:500;color:var(--bronze);text-transform:uppercase;padding-bottom:10px;border-bottom:1px solid #555}
.footer ul{position:absolute;list-style:none;font-size:13px;line-height:32px;color:#ccc}
.small{font-size:9px;line-height:12px}
</style>
</head>
<body>

<svg width="0" height="0" style="position:absolute">
  <defs>
    <symbol id="cross" viewBox="0 0 60 60"><path d="M22 4h16v18h18v16H38v18H22V38H4V22h18z"/></symbol>
    <symbol id="scales" viewBox="0 0 60 60"><g fill="none" stroke="currentColor" stroke-width="3" stroke-linecap="round"><path d="M30 6v46M16 54h28M10 14h40"/><path d="M10 14 3 32h14zM50 14l-7 18h14z"/><path d="M3 32a7 5 0 0 0 14 0M43 32a7 5 0 0 0 14 0"/></g></symbol>
    <symbol id="pulse" viewBox="0 0 60 60"><path fill="none" stroke="currentColor" stroke-width="3" stroke-linejoin="round" d="M2 32h14l6-14 8 26 6-18 4 6h18"/></symbol>
  </defs>
</svg>

<header class="site-header">
  <div class="brand"><span class="mark"></span><div>MERIDALE<small>CIRCLE</small></div></div>
  <div class="topbar">
    <span class="phone"><svg width="22" height="22" viewBox="0 0 24 24"><path fill="#fff" d="M6.6 10.8a15 15 0 0 0 6.6 6.6l2.2-2.2c.3-.3.7-.4 1-.2 1.1.4 2.3.6 3.6.6.6 0 1 .4 1 1V20c0 .6-.4 1-1 1A17 17 0 0 1 3 4c0-.6.4-1 1-1h3.5c.6 0 1 .4 1 1 0 1.3.2 2.5.6 3.6.1.3 0 .7-.2 1z"/></svg>(800) 555-0142</span>
    <span class="join">JOIN US NOW</span>
  </div>
  <nav class="nav"><span class="active">HOME</span><span>ABOUT</span><span>SERVICES</span><span>TEAM</span><span>CAREER</span><span>BLOG</span></nav>
  <div class="login">LOGIN</div>
</header>

<section class="hero">
  <div class="abs" role="img" aria-label="Black and white photo of a hospital corridor with a splash of bronze" style="left:420px;top:0;width:780px;height:745px;background:linear-gradient(90deg,rgba(244,244,244,0),rgba(90,90,90,.35) 50%,rgba(200,200,200,.2))"></div>
  <h1>The Meridale<br>Circle</h1>
  <div class="slogan">Stewards of a Fair and Prompt Outcome</div>
  <p>We have custom programs to help your medical practice grow, whether you are a newly appointed physician or a long-time practitioner</p>
  <div class="btn" style="left:36px;top:440px;width:180px;height:42px;font-size:18px">Join Us Now</div>
  <div class="btn" style="left:230px;top:440px;width:176px;height:42px;font-size:18px;background:#9a9a9a">Start Now</div>
  <span class="dot" style="left:36px"></span><span class="dot" style="left:81px;background:var(--bronze)"></span><span class="dot" style="left:127px"></span>
  <svg class="abs" style="left:0;top:560px" width="1200" height="186" viewBox="0 0 1200 186"><path fill="#fff" d="M0 186V150C250 190 460 200 700 110C900 40 1080 60 1200 110V186Z"/></svg>
</section>

<section>
  <div class="symbol steel" style="left:58px;top:985px;width:355px;height:260px;border-radius:14px;color:#e3e3e3" role="img" aria-label="Scales of justice symbol"><svg width="110" height="110"><use href="#scales"/></svg></div>
  <div class="symbol silver" style="left:278px;top:1137px;width:268px;height:198px;border-radius:10px;border:3px solid #fff;fill:var(--bronze)" role="img" aria-label="Medical cross symbol"><svg width="72" height="72"><use href="#cross"/></svg></div>
  <h2 class="h2 about-title">About<br>Meridale Circle</h2>
  <p class="about-copy">The Meridale Circle is a leader in Qualified Medical Evaluations and SIBTF cases in the State of California. Our doctors are dedicated facilitating settlements through rapid, objective and well researched Expert Medical Opinions<br>We provide honest and ethical exams maintaining integrity and respect within our community.</p>
  <div class="btn" style="left:622px;top:1255px;width:156px;height:34px;font-size:13px">More About Us</div>

  <div class="features">
    <div class="feature" style="left:45px">
      <svg width="52" height="70" viewBox="0 0 52 70" fill="none" stroke="#a3412a" stroke-width="2"><circle cx="20" cy="20" r="11"/><path d="M2 68V50c0-8 8-13 18-13s18 5 18 13v18"/><path d="M14 40v12M26 40v12"/><rect x="32" y="6" width="18" height="12" rx="3"/></svg>
      <div><h3>Get Assistance From<br>A Medical Expert</h3><p>Medical-Legal Experts are here to<br>help you in all the various specialties.</p></div>
    </div>
    <div class="feature" style="left:390px">
      <svg width="52" height="70" viewBox="0 0 52 70" fill="none" stroke="#a3412a" stroke-width="2"><rect x="6" y="4" width="40" height="62" rx="3"/><path d="M14 18h6M14 30h6M14 42h6M14 54h6M26 18h12M26 30h12M26 42h12M26 54h12"/></svg>
      <div><h3>QME Report Writing<br>Courses &amp; More</h3><p>Medical-Legal Experts are here to<br>help you in all the various specialties.</p></div>
    </div>
    <div class="feature" style="left:722px">
      <svg width="70" height="70" viewBox="0 0 70 70" fill="none" stroke="#a3412a" stroke-width="2"><circle cx="35" cy="35" r="9"/><circle cx="35" cy="8" r="6"/><circle cx="35" cy="62" r="6"/><circle cx="8" cy="22" r="6"/><circle cx="62" cy="22" r="6"/><circle cx="8" cy="48" r="6"/><circle cx="62" cy="48" r="6"/><path d="M35 14v12M35 44v12M13 25l14 6M57 25l-14 6M13 45l14-6M57 45l-14-6"/></svg>
      <div><h3>Join Our Expert<br>Team Now</h3><p>Medical-Legal Experts are here to<br>help you in all the various specialties.</p></div>
    </div>
  </div>
</section>

<section>
  <div class="wwd"></div>
  <h2 class="h2" style="left:0;right:0;top:1664px;text-align:center;font-size:34px">What We Do</h2>
  <p class="section-sub" style="top:1734px">We provide exceptional nationwide service of Medical-Legal Examinations (IME, QME &amp; AME), Peer Reviews, Record Reviews, Functional Capacity Evaluations (FCE), Expert Witness Testimony, and Subsequent Injuries Benefit Trust Fund (SIBTF) eligibility determinations.</p>
  <svg class="arrow" style="left:36px" width="54" height="54" viewBox="0 0 54 54" fill="none" stroke="#a3412a" stroke-width="3"><circle cx="27" cy="27" r="24"/><path d="M38 27H16M25 18l-9 9 9 9"/></svg>
  <svg class="arrow" style="left:1100px" width="54" height="54" viewBox="0 0 54 54" fill="none" stroke="#a3412a" stroke-width="3"><circle cx="27" cy="27" r="24"/><path d="M16 27h22M29 18l9 9-9 9"/></svg>
  <div class="card" style="left:165px;top:1843px">
    <div class="symbol steel" style="color:#e6e6e6" role="img" aria-label="Pulse line symbol"><svg width="90" height="90"><use href="#pulse"/></svg></div>
    <h3>Expert Source<br>Methodology</h3>
    <p>Our proprietary Expert Source method saves you time, increases your success rate, and gets you answers to complex disputed medical issues.</p>
    <div class="btn">Read More</div>
  </div>
  <div class="card" style="left:497px;top:1843px">
    <div class="symbol silver" style="fill:var(--bronze)" role="img" aria-label="Medical cross symbol"><svg width="70" height="70"><use href="#cross"/></svg></div>
    <h3>Extensive Medical<br>Expert Network</h3>
    <p>Our proprietary Expert Source method saves you time, increases your success rate, and gets you answers to complex disputed medical issues.</p>
    <div class="btn">Read More</div>
  </div>
  <div class="card" style="left:827px;top:1843px">
    <div class="symbol bronze" style="color:#f1e6e2" role="img" aria-label="Scales of justice symbol"><svg width="90" height="90"><use href="#scales"/></svg></div>
    <h3>Medical-Legal<br>Service</h3>
    <p>Our proprietary Expert Source method saves you time, increases your success rate, and gets you answers to complex disputed medical issues.</p>
    <div class="btn">Read More</div>
  </div>
</section>

<section>
  <h2 class="h2 std-title">Highest Standard in<br>Medical Reporting</h2>
  <ul class="std-list">
    <li><svg width="16" height="16" viewBox="0 0 16 16" fill="none" stroke="#a3412a" stroke-width="1.5"><circle cx="8" cy="8" r="7"/><path d="M5 8h6M8.5 5.5 11 8l-2.5 2.5"/></svg>Timely: Unless special circumstances exist, you can expect to receive the report well ahead of DWC imposed deadlines</li>
    <li><svg width="16" height="16" viewBox="0 0 16 16" fill="none" stroke="#a3412a" stroke-width="1.5"><circle cx="8" cy="8" r="7"/><path d="M5 8h6M8.5 5.5 11 8l-2.5 2.5"/></svg>Clear, Concise and Readable: So your valuable time is not wasted</li>
    <li><svg width="16" height="16" viewBox="0 0 16 16" fill="none" stroke="#a3412a" stroke-width="1.5"><circle cx="8" cy="8" r="7"/><path d="M5 8h6M8.5 5.5 11 8l-2.5 2.5"/></svg>Impartial: (all of our reports are reviewed by a 3rd party for Objectivity</li>
    <li><svg width="16" height="16" viewBox="0 0 16 16" fill="none" stroke="#a3412a" stroke-width="1.5"><circle cx="8" cy="8" r="7"/><path d="M5 8h6M8.5 5.5 11 8l-2.5 2.5"/></svg>High Level Review of Records by the Physician with Commentary</li>
    <li><svg width="16" height="16" viewBox="0 0 16 16" fill="none" stroke="#a3412a" stroke-width="1.5"><circle cx="8" cy="8" r="7"/><path d="M5 8h6M8.5 5.5 11 8l-2.5 2.5"/></svg>Detailed and Comprehensive Medical History</li>
    <li><svg width="16" height="16" viewBox="0 0 16 16" fill="none" stroke="#a3412a" stroke-width="1.5"><circle cx="8" cy="8" r="7"/><path d="M5 8h6M8.5 5.5 11 8l-2.5 2.5"/></svg>Answers to all questions stated in the Cover Letter</li>
  </ul>
  <div class="btn" style="left:110px;top:2701px;width:112px;height:32px;font-size:13px">Read More</div>
  <div class="abs" style="left:690px;top:2353px;width:402px;height:290px;background:var(--bronze);border-radius:10px"></div>
  <div class="symbol steel" style="left:660px;top:2378px;width:410px;height:310px;border-radius:10px;color:#e6e6e6;gap:40px" role="img" aria-label="Medical and legal symbols"><svg width="90" height="90" style="fill:#e6e6e6"><use href="#cross"/></svg><svg width="110" height="110"><use href="#scales"/></svg></div>
</section>

<section class="team">
  <h2 class="h2" style="left:0;right:0;top:78px;text-align:center;font-size:34px">Meet Our Team</h2>
  <div class="member" style="left:55px"><div class="initials">JD</div><h4>JOHN DOE</h4><span>Senior Doctor</span></div>
  <div class="member" style="left:336px"><div class="initials">JD</div><h4>JOHN DOE</h4><span>Senior Doctor</span></div>
  <div class="member" style="left:617px"><div class="initials">JD</div><h4>JOHN DOE</h4><span>Senior Doctor</span></div>
  <div class="member" style="left:898px"><div class="initials">JD</div><h4>JOHN DOE</h4><span>Senior Doctor</span></div>
</section>
<span class="tdot" style="left:537px"></span><span class="tdot" style="left:582px;background:var(--bronze)"></span><span class="tdot" style="left:628px"></span>

<section class="contact">
  <div class="abs" role="img" aria-label="Map of California divided into northern, central and southern regions" style="left:60px;top:80px;width:510px;height:540px;background:linear-gradient(160deg,#8a8a8a,#5f5f5f 50%,#6e6e6e);opacity:.85"></div>
  <div class="region" style="left:110px;top:210px">Northern<br>California<small>See Locations</small></div>
  <div class="region" style="left:265px;top:410px">Central<br>California<small>See Locations</small></div>
  <div class="region" style="left:393px;top:540px">Southern<br>California<small>See Locations</small></div>
</section>
<div class="form-card">
  <h2>GET IN TOUCH</h2>
  <div class="field" style="top:107px;height:60px">NAME</div>
  <div class="field" style="top:191px;height:60px">EMAIL</div>
  <div class="field" style="top:280px;height:118px;padding-top:18px">MESSAGE</div>
  <div class="btn submit">Submit Now</div>
</div>

<section>
  <h2 class="h2" style="left:0;right:0;top:4130px;text-align:center;font-size:34px">Latest From Blog</h2>
  <article class="post" style="left:115px">
    <div class="symbol steel" style="color:#e6e6e6" role="img" aria-label="Pulse line symbol"><svg width="80" height="80"><use href="#pulse"/></svg></div>
    <h3>BLOG POST 2</h3>
    <p>Examines the spinal cord and surrounding structures to identify issues like herniated discs, spinal cord injuries, or tumors.</p>
    <a>READ MORE ⟶</a>
  </article>
  <article class="post" style="left:452px">
    <div class="symbol silver" style="fill:var(--bronze)" role="img" aria-label="Medical cross symbol"><svg width="64" height="64"><use href="#cross"/></svg></div>
    <h3>BLOG POST 3</h3>
    <p>Focuses on joints, bones, and soft tissues, helping diagnose conditions like ligament tears, arthritis, or sports injuries.</p>
    <a>READ MORE ⟶</a>
  </article>
  <article class="post" style="left:790px">
    <div class="symbol steel" style="color:#e6e6e6" role="img" aria-label="Scales of justice symbol"><svg width="80" height="80"><use href="#scales"/></svg></div>
    <h3>BLOG POST 4</h3>
    <p>Used to detect abnormalities in the brain, such as tumors, strokes, or injuries.</p>
    <a>READ MORE ⟶</a>
  </article>
</section>

<footer class="footer">
  <div class="brand" style="left:60px;top:92px"><span class="mark"></span><div>MERIDALE<small>CIRCLE</small></div></div>
  <div class="abs" style="left:72px;top:224px;font-size:13px;color:#ccc;display:flex;gap:24px;align-items:center">FOLLOW US
    <span style="width:16px;height:16px;border-radius:50%;background:var(--bronze)"></span>
    <span style="width:16px;height:16px;border-radius:50%;background:var(--bronze)"></span>
    <span style="width:16px;height:16px;border-radius:50%;background:var(--bronze)"></span></div>
  <h5 style="left:452px;width:150px">Quick Links</h5>
  <ul style="left:458px;top:148px"><li>HOME</li><li>ABOUT US</li><li>SERVICES</li><li>CONTACT</li></ul>
  <h5 style="left:686px;width:146px">Contact</h5>
  <div class="abs" style="left:694px;top:152px;display:flex;gap:12px"><span style="width:20px;height:20px;border-radius:50%;background:#ddd"></span><div class="small"><span style="color:var(--bronze)">Call toll free</span><br>(800) 555-0142</div></div>
  <div class="abs" style="left:694px;top:190px;display:flex;gap:12px"><span style="width:20px;height:20px;border-radius:50%;background:#ddd"></span><div class="small"><span style="color:var(--bronze)">Fax</span><br>(800) 555-0143</div></div>
  <span class="abs" style="left:694px;top:232px;width:20px;height:20px;border-radius:50%;background:#ddd"></span>
  <h5 style="left:947px;width:190px">Newsletter</h5>
  <div class="abs small" style="left:950px;top:152px;color:#999">Join our Newsletter to<br>Stay Updated</div>
  <div class="abs" style="left:948px;top:190px;width:96px;height:18px;background:#fff;color:#777;font-size:8px;padding:4px 6px">Email Address</div>
  <div class="abs" style="left:1044px;top:190px;width:84px;height:18px;background:var(--bronze);color:#fff;font-size:9px;display:flex;align-items:center;justify-content:center">SUBSCRIBE</div>
  <div class="abs" style="left:70px;top:342px;font-size:11px;color:#555">Copyright 2024, All Rights Reserved</div>
  <div class="abs" style="left:882px;top:342px;font-size:11px;color:#555">Privacy Policy &nbsp;|&nbsp; Terms and Conditions</div>
</footer>

</body>
</html>
```